依頼詳細
比較する栄養素が多いので、どうすればお客様に見て頂きやすいか、
スマホで見た時に伝わりやすいかを重視したデザインにしていただきたいです。

添付している「参考画像」のようなグラフにしようと思ったのですが、
横長に作られており、スマホで見ると文字が小さくなって見づらいのではと思い
こちらでデザインを募らせていただく事となりました。

今のLPに差し込んでも違和感のないデザインでお願いします。

なお、今回はデザインのみでコーディングは必要ありません。
サイトURL
https://tovrekline.com/lp/
ページ数
1ページ
希望イメージ
シンプル 複雑
単色 カラフル
暗い 明るい
日常 高級
遊び心 厳粛
未来的 伝統的
女性的 男性的
希望する色
青系、無彩色系
納品ファイル
• 高解像度JPG (.jpg)
• イラストレーター形式 (.ai)
• フォトショップ形式 (.psd)
補足説明
■ 選んだ理由

一番バランスの良いデザインでした。

■ 提案者全員のお礼・コメント

この度は沢山のご提案ありがとうございました。
また機会がございましたら、どうぞよろしくお願いいたします。

```html
<!DOCTYPE html>
<html lang="ja">
<head>
<meta charset="utf-8">
<title>マルチビタミンミネラル 90粒</title>
<link rel="stylesheet" href="https://fonts.googleapis.com/css2?family=Noto+Sans+JP:wght@400;500;700;900&family=Roboto+Condensed:wght@700&display=swap">
<style>
:root{
  --navy:#1b3b8c;
  --ink:#1f2a44;
  --avg:#c9d4e8;
  --generic:#8e8e8e;
  --premium:#c6c6c6;
  --axis:#9aa3b5;
  --bg:#ffffff;
  --photo-a:#eef1f6;
  --photo-b:#d6dde9;
}
*{box-sizing:border-box;margin:0;padding:0}
html,body{width:1200px;height:4804px;overflow:hidden;background:var(--bg)}
body{font-family:"Noto Sans JP",sans-serif;color:var(--ink);position:relative}
.product-photo{position:absolute;left:120px;top:40px;width:960px;height:1020px;background:linear-gradient(160deg,var(--photo-a),var(--photo-b))}
.title{position:absolute;top:1130px;left:0;width:1200px;text-align:center;color:var(--navy);font-weight:700;font-size:50px;line-height:64px;letter-spacing:2px}
.subtitle{position:absolute;top:1206px;left:0;width:1200px;text-align:center;font-family:"Roboto Condensed",sans-serif;font-weight:700;font-size:18px;line-height:24px;color:var(--ink)}
.section-heading{position:absolute;top:1290px;left:0;width:1200px;text-align:center;font-weight:700;font-size:36px;line-height:48px;color:var(--ink)}
.legend{position:absolute;top:1394px;left:0;width:1200px;display:flex;justify-content:center;gap:24px;font-size:14px;line-height:20px;color:#555;align-items:center}
.legend span{display:inline-flex;align-items:center;gap:8px}
.legend i{display:inline-block;width:20px;height:20px}
.legend .note{font-size:13px}
.sw-avg{background:var(--avg)} .sw-lab{background:var(--navy)} .sw-gen{background:var(--generic)} .sw-pre{background:var(--premium)}
.chart-grid{position:absolute;top:1470px;left:150px;width:900px;display:grid;grid-template-columns:repeat(3,300px);grid-auto-rows:310px}
.nutrient{display:flex;flex-direction:column;align-items:center}
.nutrient h3{font-size:26px;font-weight:700;color:var(--navy);height:44px;line-height:40px}
.nutrient svg{width:240px;height:240px}
.ring{fill:#fff;stroke:var(--navy);stroke-width:6}
.axis{stroke:var(--axis);stroke-width:2}
.unit{font-size:13px;fill:#555;text-anchor:middle;font-family:"Noto Sans JP",sans-serif}
.b-avg{fill:var(--avg)} .b-lab{fill:var(--navy)} .b-gen{fill:var(--generic)} .b-pre{fill:var(--premium)}
.other{position:absolute;top:3960px;left:160px;width:880px;height:590px;border:3px solid var(--navy);padding:34px 50px}
.other h4{text-align:center;font-size:24px;line-height:34px;font-weight:700;color:var(--navy);margin-bottom:34px}
.other-cols{display:grid;grid-template-columns:1fr 1fr;column-gap:60px}
.other ul{list-style:none}
.other li{display:flex;align-items:baseline;font-size:18px;line-height:52px;white-space:nowrap}
.other li .dots{flex:1;border-bottom:1px solid #bbb;margin:0 10px;transform:translateY(-6px)}
</style>
</head>
<body>
<div class="product-photo" role="img" aria-label="サプリメントのパウチ袋と錠剤の商品写真"></div>

<h1 class="title">マルチビタミンミネラル 90粒</h1>
<p class="subtitle">Multivitamin and Mineral</p>
<h2 class="section-heading">マルチビタミン成分表と含有量の比較</h2>

<div class="legend">
  <span><i class="sw-avg"></i>推奨平均値</span>
  <span><i class="sw-lab"></i>サプリミナテ</span>
  <span><i class="sw-gen"></i>一般市販サプリ</span>
  <span><i class="sw-pre"></i>KRV 高価格サプリ</span>
  <span class="note">※記載ない箇所は、含有無し</span>
</div>

<div class="chart-grid">
<div class="nutrient"><h3>ビタミンA</h3><svg viewBox="0 0 240 240"><circle class="ring" cx="120" cy="120" r="112"/><text class="unit" x="120" y="58">単位:mg</text><line class="axis" x1="58" y1="66" x2="58" y2="180"/><line class="axis" x1="58" y1="180" x2="196" y2="180"/><rect class="b-avg" x="70" y="90" width="26" height="90"/><rect class="b-lab" x="102" y="160" width="26" height="20"/><rect class="b-pre" x="166" y="110" width="26" height="70"/></svg></div>
<div class="nutrient"><h3>β-カロテン</h3><svg viewBox="0 0 240 240"><circle class="ring" cx="120" cy="120" r="112"/><text class="unit" x="120" y="58">単位:mg</text><line class="axis" x1="58" y1="66" x2="58" y2="180"/><line class="axis" x1="58" y1="180" x2="196" y2="180"/><rect class="b-lab" x="102" y="70" width="26" height="110"/></svg></div>
<div class="nutrient"><h3>ビタミンC</h3><svg viewBox="0 0 240 240"><circle class="ring" cx="120" cy="120" r="112"/><text class="unit" x="120" y="58">単位:mg</text><line class="axis" x1="58" y1="66" x2="58" y2="180"/><line class="axis" x1="58" y1="180" x2="196" y2="180"/><rect class="b-avg" x="70" y="120" width="26" height="60"/><rect class="b-lab" x="102" y="70" width="26" height="110"/><rect class="b-gen" x="134" y="140" width="26" height="40"/><rect class="b-pre" x="166" y="100" width="26" height="80"/></svg></div>

<div class="nutrient"><h3>ビタミンD3</h3><svg viewBox="0 0 240 240"><circle class="ring" cx="120" cy="120" r="112"/><text class="unit" x="120" y="58">単位:mg</text><line class="axis" x1="58" y1="66" x2="58" y2="180"/><line class="axis" x1="58" y1="180" x2="196" y2="180"/><rect class="b-avg" x="70" y="130" width="26" height="50"/><rect class="b-lab" x="102" y="150" width="26" height="30"/><rect class="b-pre" x="166" y="100" width="26" height="80"/></svg></div>
<div class="nutrient"><h3>ビタミンE</h3><svg viewBox="0 0 240 240"><circle class="ring" cx="120" cy="120" r="112"/><text class="unit" x="120" y="58">単位:mg</text><line class="axis" x1="58" y1="66" x2="58" y2="180"/><line class="axis" x1="58" y1="180" x2="196" y2="180"/><rect class="b-lab" x="102" y="70" width="26" height="110"/><rect class="b-pre" x="166" y="150" width="26" height="30"/></svg></div>
<div class="nutrient"><h3>ビタミンB1</h3><svg viewBox="0 0 240 240"><circle class="ring" cx="120" cy="120" r="112"/><text class="unit" x="120" y="58">単位:mg</text><line class="axis" x1="58" y1="66" x2="58" y2="180"/><line class="axis" x1="58" y1="180" x2="196" y2="180"/><rect class="b-avg" x="70" y="170" width="26" height="10"/><rect class="b-lab" x="102" y="70" width="26" height="110"/><rect class="b-gen" x="134" y="140" width="26" height="40"/><rect class="b-pre" x="166" y="150" width="26" height="30"/></svg></div>

<div class="nutrient"><h3>ビタミンB2</h3><svg viewBox="0 0 240 240"><circle class="ring" cx="120" cy="120" r="112"/><text class="unit" x="120" y="58">単位:mg</text><line class="axis" x1="58" y1="66" x2="58" y2="180"/><line class="axis" x1="58" y1="180" x2="196" y2="180"/><rect class="b-avg" x="70" y="170" width="26" height="10"/><rect class="b-lab" x="102" y="70" width="26" height="110"/><rect class="b-gen" x="134" y="120" width="26" height="60"/><rect class="b-pre" x="166" y="140" width="26" height="40"/></svg></div>
<div class="nutrient"><h3>ナイアシン</h3><svg viewBox="0 0 240 240"><circle class="ring" cx="120" cy="120" r="112"/><text class="unit" x="120" y="58">単位:mg</text><line class="axis" x1="58" y1="66" x2="58" y2="180"/><line class="axis" x1="58" y1="180" x2="196" y2="180"/><rect class="b-avg" x="70" y="150" width="26" height="30"/><rect class="b-lab" x="102" y="70" width="26" height="110"/><rect class="b-gen" x="134" y="160" width="26" height="20"/><rect class="b-pre" x="166" y="100" width="26" height="80"/></svg></div>
<div class="nutrient"><h3>パントテン酸</h3><svg viewBox="0 0 240 240"><circle class="ring" cx="120" cy="120" r="112"/><text class="unit" x="120" y="58">単位:mg</text><line class="axis" x1="58" y1="66" x2="58" y2="180"/><line class="axis" x1="58" y1="180" x2="196" y2="180"/><rect class="b-avg" x="70" y="160" width="26" height="20"/><rect class="b-lab" x="102" y="70" width="26" height="110"/><rect class="b-gen" x="134" y="170" width="26" height="10"/><rect class="b-pre" x="166" y="150" width="26" height="30"/></svg></div>

<div class="nutrient"><h3>ビタミンB6</h3><svg viewBox="0 0 240 240"><circle class="ring" cx="120" cy="120" r="112"/><text class="unit" x="120" y="58">単位:mg</text><line class="axis" x1="58" y1="66" x2="58" y2="180"/><line class="axis" x1="58" y1="180" x2="196" y2="180"/><rect class="b-avg" x="70" y="160" width="26" height="20"/><rect class="b-lab" x="102" y="70" width="26" height="110"/><rect class="b-gen" x="134" y="150" width="26" height="30"/><rect class="b-pre" x="166" y="140" width="26" height="40"/></svg></div>
<div class="nutrient"><h3>ビタミンB12</h3><svg viewBox="0 0 240 240"><circle class="ring" cx="120" cy="120" r="112"/><text class="unit" x="120" y="58">単位:mg</text><line class="axis" x1="58" y1="66" x2="58" y2="180"/><line class="axis" x1="58" y1="180" x2="196" y2="180"/><rect class="b-avg" x="70" y="170" width="26" height="10"/><rect class="b-lab" x="102" y="70" width="26" height="110"/><rect class="b-gen" x="134" y="140" width="26" height="40"/><rect class="b-pre" x="166" y="150" width="26" height="30"/></svg></div>
<div class="nutrient"><h3>葉酸</h3><svg viewBox="0 0 240 240"><circle class="ring" cx="120" cy="120" r="112"/><text class="unit" x="120" y="58">単位:mg</text><line class="axis" x1="58" y1="66" x2="58" y2="180"/><line class="axis" x1="58" y1="180" x2="196" y2="180"/><rect class="b-avg" x="70" y="140" width="26" height="40"/><rect class="b-lab" x="102" y="70" width="26" height="110"/><rect class="b-gen" x="134" y="140" width="26" height="40"/><rect class="b-pre" x="166" y="90" width="26" height="90"/></svg></div>

<div class="nutrient"><h3>ビオチン</h3><svg viewBox="0 0 240 240"><circle class="ring" cx="120" cy="120" r="112"/><text class="unit" x="120" y="58">単位:mg</text><line class="axis" x1="58" y1="66" x2="58" y2="180"/><line class="axis" x1="58" y1="180" x2="196" y2="180"/><rect class="b-avg" x="70" y="150" width="26" height="30"/><rect class="b-lab" x="102" y="140" width="26" height="40"/><rect class="b-gen" x="134" y="110" width="26" height="70"/><rect class="b-pre" x="166" y="90" width="26" height="90"/></svg></div>
<div class="nutrient"><h3>カルシウム</h3><svg viewBox="0 0 240 240"><circle class="ring" cx="120" cy="120" r="112"/><text class="unit" x="120" y="58">単位:mg</text><line class="axis" x1="58" y1="66" x2="58" y2="180"/><line class="axis" x1="58" y1="180" x2="196" y2="180"/><rect class="b-avg" x="70" y="80" width="26" height="100"/><rect class="b-lab" x="102" y="140" width="26" height="40"/><rect class="b-gen" x="134" y="120" width="26" height="60"/><rect class="b-pre" x="166" y="130" width="26" height="50"/></svg></div>
<div class="nutrient"><h3>マグネシウム</h3><svg viewBox="0 0 240 240"><circle class="ring" cx="120" cy="120" r="112"/><text class="unit" x="120" y="58">単位:mg</text><line class="axis" x1="58" y1="66" x2="58" y2="180"/><line class="axis" x1="58" y1="180" x2="196" y2="180"/><rect class="b-avg" x="70" y="70" width="26" height="110"/><rect class="b-lab" x="102" y="130" width="26" height="50"/><rect class="b-gen" x="134" y="160" width="26" height="20"/><rect class="b-pre" x="166" y="140" width="26" height="40"/></svg></div>

<div class="nutrient"><h3>亜鉛</h3><svg viewBox="0 0 240 240"><circle class="ring" cx="120" cy="120" r="112"/><text class="unit" x="120" y="58">単位:mg</text><line class="axis" x1="58" y1="66" x2="58" y2="180"/><line class="axis" x1="58" y1="180" x2="196" y2="180"/><rect class="b-avg" x="70" y="120" width="26" height="60"/><rect class="b-lab" x="102" y="140" width="26" height="40"/><rect class="b-gen" x="134" y="90" width="26" height="90"/><rect class="b-pre" x="166" y="90" width="26" height="90"/></svg></div>
<div class="nutrient"><h3>マンガン</h3><svg viewBox="0 0 240 240"><circle class="ring" cx="120" cy="120" r="112"/><text class="unit" x="120" y="58">単位:mg</text><line class="axis" x1="58" y1="66" x2="58" y2="180"/><line class="axis" x1="58" y1="180" x2="196" y2="180"/><rect class="b-avg" x="70" y="90" width="26" height="90"/><rect class="b-lab" x="102" y="110" width="26" height="70"/><rect class="b-pre" x="166" y="90" width="26" height="90"/></svg></div>
<div class="nutrient"><h3>クロム</h3><svg viewBox="0 0 240 240"><circle class="ring" cx="120" cy="120" r="112"/><text class="unit" x="120" y="58">単位:mg</text><line class="axis" x1="58" y1="66" x2="58" y2="180"/><line class="axis" x1="58" y1="180" x2="196" y2="180"/><rect class="b-avg" x="70" y="100" width="26" height="80"/><rect class="b-lab" x="102" y="150" width="26" height="30"/><rect class="b-gen" x="134" y="110" width="26" height="70"/><rect class="b-pre" x="166" y="90" width="26" height="90"/></svg></div>

<div class="nutrient"><h3>セレン</h3><svg viewBox="0 0 240 240"><circle class="ring" cx="120" cy="120" r="112"/><text class="unit" x="120" y="58">単位:mg</text><line class="axis" x1="58" y1="66" x2="58" y2="180"/><line class="axis" x1="58" y1="180" x2="196" y2="180"/><rect class="b-avg" x="70" y="100" width="26" height="80"/><rect class="b-lab" x="102" y="160" width="26" height="20"/><rect class="b-gen" x="134" y="80" width="26" height="100"/><rect class="b-pre" x="166" y="90" width="26" height="90"/></svg></div>
<div class="nutrient"><h3>銅</h3><svg viewBox="0 0 240 240"><circle class="ring" cx="120" cy="120" r="112"/><text class="unit" x="120" y="58">単位:mg</text><line class="axis" x1="58" y1="66" x2="58" y2="180"/><line class="axis" x1="58" y1="180" x2="196" y2="180"/><rect class="b-lab" x="102" y="80" width="26" height="100"/><rect class="b-gen" x="134" y="150" width="26" height="30"/><rect class="b-pre" x="166" y="130" width="26" height="50"/></svg></div>
<div class="nutrient"><h3>モリブデン</h3><svg viewBox="0 0 240 240"><circle class="ring" cx="120" cy="120" r="112"/><text class="unit" x="120" y="58">単位:mg</text><line class="axis" x1="58" y1="66" x2="58" y2="180"/><line class="axis" x1="58" y1="180" x2="196" y2="180"/><rect class="b-avg" x="70" y="100" width="26" height="80"/><rect class="b-lab" x="102" y="160" width="26" height="20"/><rect class="b-gen" x="134" y="110" width="26" height="70"/><rect class="b-pre" x="166" y="110" width="26" height="70"/></svg></div>

<div class="nutrient"><h3>イノシトール</h3><svg viewBox="0 0 240 240"><circle class="ring" cx="120" cy="120" r="112"/><text class="unit" x="120" y="58">単位:mg</text><line class="axis" x1="58" y1="66" x2="58" y2="180"/><line class="axis" x1="58" y1="180" x2="196" y2="180"/><rect class="b-lab" x="102" y="70" width="26" height="110"/></svg></div>
</div>

<section class="other">
  <h4>マルチビタミンに含まれるその他の成分</h4>
  <div class="other-cols">
    <ul>
      <li>コリン<span class="dots"></span>4mg</li>
      <li>L-シスチン<span class="dots"></span>20mg</li>
      <li>L-トリプトファン<span class="dots"></span>40mg</li>
      <li>L-メチオニン<span class="dots"></span>3mg</li>
      <li>ルテイン<span class="dots"></span>1mg</li>
      <li>リコペン<span class="dots"></span>1mg</li>
      <li>ゼアキサンチン<span class="dots"></span>1mg</li>
      <li>パイナップル抽出物<span class="dots"></span>25mg</li>
    </ul>
    <ul>
      <li>ローズヒップ抽出物<span class="dots"></span>3mg</li>
      <li>レモンバイオフラボノイド<span class="dots"></span>3mg</li>
      <li>ポリフェノール<span class="dots"></span>3mg</li>
      <li>ビタミンP<span class="dots"></span>10mg</li>
      <li>コエンザイムQ10<span class="dots"></span>10mg</li>
      <li>スピルリナ原末<span class="dots"></span>5mg</li>
      <li>パパイヤ抽出物<span class="dots"></span>25mg</li>
      <li>緑茶抽出物<span class="dots"></span>80mg</li>
    </ul>
  </div>
</section>
</body>
</html>
```